I need a professional business card to handout at networking events for my senior helper business. I would like to use the logo I have uploaded. The design should be clear and easy to read and should list the following information...
Dessa Quillan
Owner
www.BrightwayElderAssist.example
Fairhaven, Ohio
555.304.2291
Dessa@brightwayelderassist.example

Target Market(s)

Senior Citizens

Industry/Entity Type

Personal Helper/ Assisstant

Contact Information for Business Card

I have included the details in the project description box.

Font styles to use
Serif

Colors
0054AA
0677BA
7BADD7
CADEEF
E8F1F8
59FF00
82FF00
B8FF75
E3FFCB
F4FFEA
E54698
E96AAD
F1A4CE
F9D9EA
FCEFF6
6B429C
8869AF
B7A5CE
E3DAEB
F3F0F8

Requirements
Must have
• Include uploaded logo
Nice to have
• The log that has been uploaded
Should not have
• No crazy fonts

```html
<!DOCTYPE html>
<html lang="en">
<head>
<meta charset="utf-8">
<title>Brightway Elder Assist – Business Card</title>
<link href="https://fonts.googleapis.com/css2?family=Lato:wght@400;700&family=Oswald:wght@700&display=swap" rel="stylesheet">
<style>
  :root {
    --stage: #2b2b2b;
    --paper: #ffffff;
    --violet: #632ee8;
    --crimson: #d81e5b;
    --ink-light: #ffffff;
  }
  html, body {
    margin: 0;
    padding: 0;
    width: 1047px;
    height: 1200px;
    overflow: hidden;
    background: var(--stage);
  }
  .canvas {
    position: relative;
    width: 1047px;
    height: 1200px;
  }
  .card {
    position: absolute;
    left: 156px;
    width: 743px;
    height: 423px;
    border-radius: 20px;
    overflow: hidden;
    background: var(--paper);
  }
  .card--front { top: 120px; }
  .card--back  { top: 634px; }

  .front-band {
    position: absolute;
    inset: 0;
  }
  .brand-mark {
    position: absolute;
    left: 30px;
    top: 120px;
    width: 240px;
    font-family: "Lato", sans-serif;
    font-weight: 700;
    font-size: 34px;
    line-height: 1.2;
    color: var(--crimson);
  }
  .identity {
    position: absolute;
    right: 33px;
    top: 208px;
    text-align: right;
    color: var(--ink-light);
  }
  .identity__name {
    margin: 0;
    font-family: "Oswald", sans-serif;
    font-weight: 700;
    font-size: 37px;
    line-height: 42px;
    letter-spacing: 0.5px;
  }
  .identity__role {
    margin: 0;
    font-family: "Lato", sans-serif;
    font-size: 20px;
    line-height: 26px;
  }
  .contact {
    position: absolute;
    right: 33px;
    top: 292px;
    margin: 0;
    padding: 0;
    list-style: none;
    font-family: "Lato", sans-serif;
    font-size: 18px;
    color: var(--ink-light);
  }
  .contact__item {
    display: flex;
    justify-content: flex-end;
    align-items: center;
    height: 26.3px;
    gap: 13px;
  }
  .contact__icon {
    width: 18px;
    height: 18px;
    flex: none;
  }
  .back-brand {
    position: absolute;
    left: 0;
    right: 0;
    top: 186px;
    display: flex;
    justify-content: center;
    align-items: center;
    gap: 16px;
    font-family: "Lato", sans-serif;
    font-weight: 400;
    font-size: 46px;
    color: var(--violet);
  }
  .back-brand__dot {
    width: 34px;
    height: 34px;
    border-radius: 50%;
    background: var(--crimson);
  }
</style>
</head>
<body>
<main class="canvas">
  <section class="card card--front" aria-label="Card front">
    <svg class="front-band" width="743" height="423" viewBox="0 0 743 423" aria-hidden="true">
      <path fill="var(--violet)" d="M331 0 C420 30 460 110 438 190 C414 268 330 300 282 330 C238 360 229 392 229 423 L743 423 L743 0 Z"/>
    </svg>
    <div class="brand-mark">Brightway<br>Elder Assist</div>
    <div class="identity">
      <h1 class="identity__name">DESSA QUILLAN</h1>
      <p class="identity__role">Owner</p>
    </div>
    <ul class="contact">
      <li class="contact__item">555.304.2291
        <svg class="contact__icon" viewBox="0 0 24 24" aria-hidden="true"><path fill="#fff" d="M6.6 10.8a15 15 0 0 0 6.6 6.6l2.2-2.2a1 1 0 0 1 1-.25 11.4 11.4 0 0 0 3.6.57 1 1 0 0 1 1 1V20a1 1 0 0 1-1 1A17 17 0 0 1 3 4a1 1 0 0 1 1-1h3.5a1 1 0 0 1 1 1c0 1.25.2 2.45.57 3.57a1 1 0 0 1-.25 1z"/></svg>
      </li>
      <li class="contact__item">Dessa@brightwayelderassist.example
        <svg class="contact__icon" viewBox="0 0 24 24" aria-hidden="true"><rect x="2" y="5" width="20" height="14" fill="none" stroke="#fff" stroke-width="2"/><path d="M2 5l10 8 10-8" fill="none" stroke="#fff" stroke-width="2"/></svg>
      </li>
      <li class="contact__item">www.BrightwayElderAssist.example
        <svg class="contact__icon" viewBox="0 0 24 24" aria-hidden="true"><circle cx="12" cy="12" r="9.5" fill="none" stroke="#fff" stroke-width="2"/><path d="M2.5 12h19M12 2.5c3 3 3 16 0 19M12 2.5c-3 3-3 16 0 19" fill="none" stroke="#fff" stroke-width="1.6"/></svg>
      </li>
      <li class="contact__item">Fairhaven, Ohio
        <svg class="contact__icon" viewBox="0 0 24 24" aria-hidden="true"><path fill="#fff" d="M12 2a7 7 0 0 0-7 7c0 5 7 13 7 13s7-8 7-13a7 7 0 0 0-7-7zm0 9.5A2.5 2.5 0 1 1 12 6.5a2.5 2.5 0 0 1 0 5z"/></svg>
      </li>
    </ul>
  </section>

  <section class="card card--back" aria-label="Card back">
    <div class="back-brand">
      <span class="back-brand__dot" aria-hidden="true"></span>
      <span class="back-brand__name">Brightway Elder Assist</span>
    </div>
  </section>
</main>
</body>
</html>
```